New book cover for existing E-Bike tour book

I would like to update the current design of my book "Pedal Trails of the Brackenmoor" (translation: Pedal Trails of the Brackenmoor) and make it more modern.

Existing Book:
Title: "Pedal trails of the Brackenmoor"
Subtitle: 40 eventful tours with nature and culture.
Info bar with three elements:
 Unique sights
 Cozy beer gardens
 The most beautiful bike paths

objectives:
- to make the design more modern
- to make it attractive for people who want to ride E-bike

Requirements for the new design:

1. All texts for title, subtitle and info bar should be kept.
Font, color and placement can be changed.

2. the 5 nature images below the title are optional: can be used, can be replaced, can be omitted

3. the background image is optional: can be used or can be replaced with a totally different background.

Target Market(s)

People who want to discover the "Odenwald" region with the E-Bike

Font styles to use
Sans Serif

Requirements
Must have
• all texts for title, subtitle and info bar should be kept.
Nice to have
• It would be nice to see two E-bike riders. Like on the original book cover but just bigger in size. The two E-Bike riders on the original cover are a bit small.

```html
<!DOCTYPE html>
<html lang="en">
<head>
<meta charset="utf-8">
<title>Pedal Trails of the Brackenmoor – Cover</title>
<link rel="stylesheet" href="https://fonts.googleapis.com/css2?family=Oswald:wght@300;400;700&family=Poppins:wght@400;500;700&display=swap">
<style>
  :root {
    --stage: #5f5f5f;
    --sky-deep: #034a72;
    --sky-mid: #2f7fa8;
    --sky-light: #7fc0d6;
    --hill: #3d6b3a;
    --meadow: #5c9a2b;
    --shadow: #0b0b0b;
    --title-yellow: #f7ea00;
    --region-blue: #3db7f5;
    --white: #ffffff;
    --badge-navy: #0b3f73;
  }
  * { box-sizing: border-box; margin: 0; padding: 0; }
  html, body {
    width: 1200px; height: 958px; overflow: hidden;
    background: var(--stage);
  }
  .stage {
    position: relative; width: 1200px; height: 958px;
    display: flex; align-items: center; justify-content: center;
  }
  .cover {
    position: relative; width: 590px; height: 886px; overflow: hidden;
    font-family: "Poppins", sans-serif; color: var(--white);
  }
  .cover__backdrop {
    position: absolute; inset: 0;
    background: linear-gradient(180deg,
      var(--sky-deep) 0%, var(--sky-mid) 22%, var(--sky-light) 40%,
      #8fc4c4 44%, var(--hill) 50%, #4e8a34 58%, var(--meadow) 66%,
      #2e5a1f 76%, #142312 88%, var(--shadow) 100%);
  }
  .author {
    position: absolute; top: 46px; left: 0; width: 100%;
    text-align: center; font-weight: 700; font-size: 26px;
    letter-spacing: 0.32em; padding-left: 0.32em;
  }
  .title {
    position: absolute; inset: 0; pointer-events: none;
    font-family: "Oswald", sans-serif; font-weight: 400; line-height: 1;
  }
  .title__main {
    position: absolute; right: 56px; top: 100px;
    color: var(--title-yellow); font-weight: 700;
    font-size: 82px; white-space: nowrap; line-height: 1;
  }
  .title__region-row {
    position: absolute; right: 66px; top: 190px;
    display: flex; align-items: flex-end; gap: 8px;
    white-space: nowrap;
  }
  .title__joiner {
    display: flex; flex-direction: column; align-items: flex-end;
    font-family: "Poppins", sans-serif; font-weight: 500;
    font-size: 28px; line-height: 0.95; padding-bottom: 6px;
  }
  .title__region {
    color: var(--region-blue); font-weight: 300; font-style: italic;
    font-size: 56px; line-height: 1.05;
  }
  .title-rule { position: absolute; left: 0; top: 0; }
  .subtitle {
    position: absolute; right: 69px; top: 271px; text-align: right;
    font-size: 16px; line-height: 1.05; font-weight: 400; text-transform: uppercase;
  }
  .gallery {
    position: absolute; left: 299px; top: 484px; width: 236px; height: 350px;
  }
  .gallery__photo {
    position: absolute; width: 119px; height: 119px;
    border: 6px solid var(--white);
  }
  .gallery__photo--ruin { left: 117px; top: 0;
    background: linear-gradient(180deg, #3f7fd0 0%, #7fb3e0 35%, #6f7f5a 50%, #4f9a30 75%, #6b645a 100%); }
  .gallery__photo--meadow { left: 0; top: 116px;
    background: linear-gradient(180deg, #c7dced 0%, #e3edf2 40%, #5f7e4a 55%, #6d9a3e 78%, #a89c88 100%); }
  .gallery__photo--lane { left: 117px; top: 116px;
    background: linear-gradient(135deg, #8b5a3c 0%, #5f8a34 40%, #4c7ab8 60%, #8a8175 100%); }
  .gallery__photo--gate { left: 0; top: 231px;
    background: linear-gradient(180deg, #3f7ec8 0%, #b56a4c 40%, #7a5a48 70%, #6d6d6d 100%); }
  .gallery__photo--street { left: 117px; top: 231px;
    background: linear-gradient(90deg, #bca690 0%, #8e7a66 40%, #595959 60%, #4f7a38 100%); }
  .badge { position: absolute; left: 53px; top: 694px; width: 80px; height: 80px; }
  .highlights {
    position: absolute; left: 56px; top: 796px; list-style: none;
    font-size: 11.5px; font-weight: 500; line-height: 17.5px; text-transform: uppercase;
  }
  .highlights li { display: flex; align-items: center; gap: 6px; }
</style>
</head>
<body>
<main class="stage">
  <section class="cover" aria-label="Book cover">
    <div class="cover__backdrop" role="img" aria-label="Background photograph of rolling green hills and wooded ridges under a clear blue sky"></div>

    <p class="author">JONAS WEIDLINGER</p>

    <h1 class="title">
      <span class="title__main">PEDAL TRAILS</span>
      <span class="title__region-row">
        <span class="title__joiner"><span>OF</span><span>THE</span></span>
        <span class="title__region">BRACKENMOOR</span>
      </span>
    </h1>

    <svg class="title-rule" width="590" height="886" aria-hidden="true">
      <line x1="534" y1="195" x2="534" y2="314" stroke="#ffffff" stroke-width="1.2"/>
      <line x1="273" y1="265" x2="534" y2="265" stroke="#ffffff" stroke-width="1.2"/>
    </svg>

    <p class="subtitle">40 eventful tours with<br>nature and culture</p>

    <div class="gallery">
      <div class="gallery__photo gallery__photo--ruin" role="img" aria-label="Photo of a castle ruin tower beside a gravel path"></div>
      <div class="gallery__photo gallery__photo--meadow" role="img" aria-label="Photo of an open meadow with distant forested hills"></div>
      <div class="gallery__photo gallery__photo--lane" role="img" aria-label="Photo of a paved lane below an old town wall"></div>
      <div class="gallery__photo gallery__photo--gate" role="img" aria-label="Photo of a stone town gate with a half-timbered tower"></div>
      <div class="gallery__photo gallery__photo--street" role="img" aria-label="Photo of a cobbled street with half-timbered houses"></div>
    </div>

    <svg class="badge" viewBox="0 0 80 80" aria-label="5th edition">
      <circle cx="40" cy="40" r="39" fill="var(--title-yellow)"/>
      <circle cx="40" cy="40" r="32" fill="none" stroke="var(--badge-navy)" stroke-width="1.3" stroke-dasharray="2 2"/>
      <text x="40" y="45" text-anchor="middle" font-family="Poppins, sans-serif" font-weight="700" font-size="24" fill="var(--badge-navy)">5TH</text>
      <text x="46" y="55" text-anchor="middle" font-family="Poppins, sans-serif" font-weight="700" font-size="7" fill="var(--badge-navy)">EDITION</text>
    </svg>

    <ul class="highlights">
      <li><svg width="8" height="9" aria-hidden="true"><polygon points="0,0 8,4.5 0,9" fill="var(--title-yellow)"/></svg>Unique sights</li>
      <li><svg width="8" height="9" aria-hidden="true"><polygon points="0,0 8,4.5 0,9" fill="var(--title-yellow)"/></svg>Cozy beer gardens</li>
      <li><svg width="8" height="9" aria-hidden="true"><polygon points="0,0 8,4.5 0,9" fill="var(--title-yellow)"/></svg>The most beautiful bike paths</li>
    </ul>
  </section>
</main>
</body>
</html>
```